Building Company Business Card Design

Need a design for a business card:
It needs to have: Name, Phone, Facebook link, Website, email
i would also like a list of works we undertake:
-New Homes
-Extensions, Renovations & Bathrooms
-Decking, Carports, Sheds (Residential and Industrial)
-Carpentry
-Fences, Patios & Pergolas

Contact Information for Business Card

Name, Phone, Facebook link, Website, email + details of services provided listed in description

```html
<!DOCTYPE html>
<html lang="en">
<head>
<meta charset="utf-8">
<title>Ridgeline Homes – Business Card</title>
<link rel="stylesheet" href="https://fonts.googleapis.com/css2?family=Ubuntu:wght@400;500;700&display=swap">
<style>
  :root {
    --green: #35b34a;
    --ink: #222222;
    --mark-grey: #3a3a3a;
    --card-dark: #0b0b0c;
    --paper: #ffffff;
    --backdrop: #e9e8ea;
  }
  * { margin: 0; padding: 0; box-sizing: border-box; }
  html, body { width: 1200px; height: 1108px; overflow: hidden; }
  body {
    background: var(--backdrop);
    font-family: "Ubuntu", sans-serif;
    position: relative;
  }
  .card {
    position: absolute;
    left: 229px;
    width: 755px;
    overflow: hidden;
  }
  .card-band {
    position: absolute;
    left: 0; right: 0; bottom: 0;
    background: var(--green);
  }

  /* Front */
  .card-front { top: 56px; height: 461px; background: var(--paper); }
  .card-front .card-band { height: 23px; }
  .brand-front {
    position: absolute;
    left: 96px; top: 200px;
    width: 260px;
    text-align: center;
    color: var(--mark-grey);
    font-weight: 500;
  }
  .brand-square {
    display: block;
    margin: 0 auto 10px;
    width: 34px; height: 34px;
    background: var(--green);
  }
  .brand-name { font-size: 26px; letter-spacing: 0.5px; line-height: 1; }
  .brand-sub { font-size: 12.5px; letter-spacing: 0.6px; line-height: 1.3; margin-top: 2px; }

  .contact-divider {
    position: absolute;
    left: 376px; top: 157px;
    width: 2px; height: 182px;
    background: var(--green);
  }
  .contact {
    position: absolute;
    left: 391px; top: 155px;
  }
  .contact-name {
    color: var(--green);
    font-weight: 700;
    font-size: 29px;
    line-height: 1.1;
  }
  .contact-title {
    color: var(--ink);
    font-size: 17px;
    margin-top: 4px;
    margin-bottom: 14px;
  }
  .contact-list { list-style: none; }
  .contact-list li {
    display: flex;
    align-items: center;
    gap: 8px;
    color: var(--ink);
    font-size: 17px;
    height: 30px;
  }
  .contact-list svg { width: 17px; height: 17px; flex: none; }

  /* Back */
  .card-back { top: 575px; height: 444px; background: var(--card-dark); }
  .card-back .card-band { height: 20px; }
  .brand-back {
    position: absolute;
    left: 0; right: 0; top: 88px;
    text-align: center;
    color: var(--paper);
    font-weight: 500;
  }
  .brand-back .brand-square { width: 44px; height: 44px; margin-bottom: 20px; }
  .brand-back .brand-name { font-size: 40px; letter-spacing: 1px; }
  .brand-back .brand-sub { font-size: 21px; letter-spacing: 1px; margin-top: 3px; }

  .services {
    position: absolute;
    left: 0; right: 0; top: 266px;
    text-align: center;
  }
  .services-heading {
    display: inline-block;
    color: var(--green);
    font-size: 20px;
    font-weight: 500;
    padding: 0 4px 4px;
    border-bottom: 2px solid var(--paper);
    margin-bottom: 14px;
  }
  .services-row {
    color: var(--paper);
    font-size: 17px;
    font-weight: 500;
    line-height: 30.5px;
  }
  .service::before {
    content: "";
    display: inline-block;
    width: 7px; height: 7px;
    border-radius: 50%;
    background: var(--green);
    margin: 0 6px 3px 0;
    vertical-align: middle;
  }
  .service + .service { margin-left: 6px; }
</style>
</head>
<body>

<section class="card card-front">
  <div class="brand-front">
    <span class="brand-square"></span>
    <div class="brand-name">RIDGELINE HOMES</div>
    <div class="brand-sub">AND DEVELOPMENTS PTY LTD</div>
  </div>

  <div class="contact-divider"></div>

  <div class="contact">
    <div class="contact-name">Daniel Hartley</div>
    <div class="contact-title">Managing Director</div>
    <ul class="contact-list">
      <li>
        <svg viewBox="0 0 24 24" aria-hidden="true"><path fill="#35b34a" d="M6.6 10.8a15.1 15.1 0 0 0 6.6 6.6l2.2-2.2c.3-.3.7-.4 1-.2 1.1.4 2.3.6 3.6.6.6 0 1 .4 1 1V20c0 .6-.4 1-1 1A17 17 0 0 1 3 4c0-.6.4-1 1-1h3.5c.6 0 1 .4 1 1 0 1.3.2 2.5.6 3.6.1.3 0 .7-.2 1z"/></svg>
        555-310-2948
      </li>
      <li>
        <svg viewBox="0 0 24 24" aria-hidden="true"><rect x="2" y="5" width="20" height="14" rx="1.5" fill="#35b34a"/><path d="M3 6.5l9 6.5 9-6.5" fill="none" stroke="#fff" stroke-width="1.6"/></svg>
        info@your websitename.com
      </li>
      <li>
        <svg viewBox="0 0 24 24" aria-hidden="true"><circle cx="12" cy="12" r="10" fill="#35b34a"/><path d="M2 12h20M12 2c3 3 3 17 0 20M12 2c-3 3-3 17 0 20" fill="none" stroke="#fff" stroke-width="1.4"/></svg>
        www.your websitename.com
      </li>
      <li>
        <svg viewBox="0 0 24 24" aria-hidden="true"><circle cx="12" cy="12" r="10" fill="#35b34a"/></svg>
        www.yoursocialpage.com
      </li>
    </ul>
  </div>

  <div class="card-band"></div>
</section>

<section class="card card-back">
  <div class="brand-back">
    <span class="brand-square"></span>
    <div class="brand-name">RIDGELINE HOMES</div>
    <div class="brand-sub">AND DEVELOPMENTS PTY LTD</div>
  </div>

  <div class="services">
    <div class="services-heading">Our Services</div>
    <div class="services-row"><span class="service">New Homes</span><span class="service">Extensions, Renovations &amp; Bathrooms</span></div>
    <div class="services-row"><span class="service">Decking, Carports, Sheds (Residential and Industrial)</span></div>
    <div class="services-row"><span class="service">Carpentry</span><span class="service">Fences, Patios &amp; Pergolas</span></div>
  </div>

  <div class="card-band"></div>
</section>

</body>
</html>
```